Construction company stationary design

We're wanting to develop a new professional stationary set for a newly establised property related business using our existing logo (attached). Business incorporates renovations, property investment and property development.

Specifically needing letter head, business cards, envelopes, email signature and need to get tshirt and caps embroydered.

Looking for something quite modern but professional using white, black and green.

Investment

```html
<!DOCTYPE html>
<html lang="en">
<head>
<meta charset="utf-8">
<title>Ridgeline Builds – Business Card</title>
<link href="https://fonts.googleapis.com/css2?family=Open+Sans:wght@400;600;700;800&display=swap" rel="stylesheet">
<style>
  :root {
    --green: #8cc63f;
    --charcoal: #3b3b3b;
    --ink: #222222;
    --grey-text: #6d6d6d;
    --paper: #ffffff;
    --backdrop: #d9d9d9;
  }
  * { margin: 0; padding: 0; box-sizing: border-box; }
  html, body { width: 1200px; height: 800px; overflow: hidden; }
  body {
    background: var(--backdrop);
    font-family: "Open Sans", Arial, sans-serif;
    position: relative;
  }
  .card {
    position: absolute;
    width: 560px;
    height: 320px;
    border-radius: 34px;
    box-shadow: 0 6px 18px rgba(0,0,0,0.18);
  }

  /* Back face */
  .card-back {
    left: 600px;
    top: 70px;
    background: var(--charcoal);
    display: flex;
    flex-direction: column;
    align-items: center;
    justify-content: center;
    gap: 22px;
  }
  .brand-mark {
    display: flex;
    align-items: center;
    gap: 14px;
  }
  .brand-mark .brand-square {
    width: 30px; height: 30px;
    background: var(--green);
  }
  .brand-name {
    color: var(--green);
    font-weight: 800;
    font-size: 44px;
    letter-spacing: 0.5px;
    line-height: 1;
  }
  .website {
    color: var(--paper);
    font-weight: 700;
    font-size: 20px;
  }
  .social-row { display: flex; gap: 8px; }
  .social-row span {
    width: 20px; height: 20px;
    border-radius: 3px;
    background: var(--green);
  }

  /* Front face */
  .card-front {
    left: 60px;
    top: 420px;
    background: var(--paper);
    display: flex;
    padding: 40px 36px 34px 40px;
  }
  .front-brand {
    width: 230px;
    display: flex;
    align-items: center;
  }
  .front-brand .brand-name {
    font-size: 46px;
    line-height: 1.02;
  }
  .contact {
    flex: 1;
    padding-left: 20px;
    color: var(--grey-text);
    font-size: 15px;
  }
  .person-name {
    color: var(--ink);
    font-weight: 700;
    font-size: 22px;
    line-height: 1.1;
  }
  .person-role {
    color: var(--green);
    font-size: 17px;
    margin-bottom: 6px;
  }
  .line {
    display: flex;
    align-items: center;
    gap: 8px;
    line-height: 1.45;
  }
  .line svg { width: 14px; height: 14px; flex: none; fill: var(--green); }
  .address { margin: 18px 0 6px; line-height: 1.3; }
  .office-email { color: var(--green); margin-top: 4px; }
</style>
</head>
<body>

<section class="card card-back">
  <div class="brand-mark">
    <span class="brand-square"></span>
    <span class="brand-name">Ridgeline Builds</span>
  </div>
  <div class="website">www.ridgelinebuilds.com</div>
  <div class="social-row" aria-label="Social media links">
    <span></span><span></span><span></span><span></span>
  </div>
</section>

<section class="card card-front">
  <div class="front-brand">
    <span class="brand-name">Ridgeline Builds</span>
  </div>
  <div class="contact">
    <div class="person-name">Daniel Mercer</div>
    <div class="person-role">Director</div>
    <div class="line">
      <svg viewBox="0 0 14 14" aria-hidden="true"><rect x="1" y="3" width="12" height="8" rx="1"/></svg>
      daniel@ridgelinebuilds.com
    </div>
    <div class="line">
      <svg viewBox="0 0 14 14" aria-hidden="true"><rect x="4" y="1" width="6" height="12" rx="1"/></svg>
      123-456-7890
    </div>
    <div class="address">Office #, Building #, Street<br>City, Country XXXXX</div>
    <div class="line">
      <svg viewBox="0 0 14 14" aria-hidden="true"><circle cx="7" cy="7" r="6"/></svg>
      123-456-7890
    </div>
    <div class="line">
      <svg viewBox="0 0 14 14" aria-hidden="true"><rect x="2" y="5" width="10" height="7" rx="1"/><rect x="4" y="1" width="6" height="4"/></svg>
      123-456-7890
    </div>
    <div class="office-email">info@ridgelinebuilds.com</div>
  </div>
</section>

</body>
</html>
```